Structural Engineering Business Card

Veltrow Drafts does residential house plans for clients in Central Florida. Would like simple but elegant business card that is appropriate for a house plan engineering company. Prefer black business card with black/white them but open to other shades of blue. I uploaded a sample card that I came across that looked good but please come up with your own creative designs.

Contact Information for Business Card

Name, Title, Phone, Email, Address, website

```html
<!DOCTYPE html>
<html lang="en">
<head>
<meta charset="utf-8">
<title>Veltrow Drafts — Business Card</title>
<link href="https://fonts.googleapis.com/css2?family=Montserrat:wght@400;700;800&display=swap" rel="stylesheet">
<style>
  :root {
    --stage: #2b2d31;
    --card-navy: #0b1a33;
    --card-deep: #081122;
    --card-ink: #070d1a;
    --blueprint-blue: rgba(29, 58, 110, 0.5);
    --blueprint-teal: rgba(31, 95, 107, 0.55);
    --blueprint-faint: rgba(29, 58, 110, 0.32);
    --accent-teal: #1aa39a;
    --text-white: #ffffff;
    --text-soft: #d6dce6;
  }
  * { box-sizing: border-box; margin: 0; padding: 0; }
  html, body {
    width: 1200px; height: 817px; overflow: hidden;
    background: var(--stage);
    font-family: "Montserrat", sans-serif;
  }
  .stage {
    width: 1200px; height: 817px;
    display: flex; align-items: center; justify-content: center; gap: 50px;
  }
  .card {
    position: relative;
    width: 525px; height: 300px;
    border-radius: 26px;
    overflow: hidden;
    box-shadow: 0 18px 40px rgba(0,0,0,0.5);
  }
  .card--front {
    background: linear-gradient(135deg, var(--card-navy) 0%, var(--card-deep) 70%, var(--card-ink) 100%);
  }
  .card--back {
    background: linear-gradient(160deg, var(--card-deep) 0%, var(--card-ink) 100%);
  }
  .blueprint-art {
    position: absolute;
    inset: 0;
  }
  .card--front .blueprint-art {
    background: radial-gradient(ellipse 62% 75% at 32% 58%, var(--blueprint-teal) 0%, var(--blueprint-blue) 40%, rgba(11,26,51,0) 100%);
  }
  .card--back .blueprint-art {
    background: radial-gradient(ellipse 40% 55% at 78% 60%, var(--blueprint-faint) 0%, rgba(11,26,51,0) 100%);
  }
  .brand {
    position: absolute;
    display: flex; align-items: center; gap: 10px;
    color: var(--text-white);
    font-weight: 800;
    font-size: 27px;
    letter-spacing: 0.5px;
    text-transform: uppercase;
    white-space: nowrap;
  }
  .brand__mark {
    width: 14px; height: 14px; background: var(--text-white);
  }
  .card--front .brand { right: 36px; top: 132px; }
  .card--back .brand { right: 40px; top: 36px; }
  .holder {
    position: absolute; left: 40px; top: 98px;
  }
  .holder__name {
    color: var(--text-white);
    font-weight: 700; font-size: 19px; letter-spacing: 0.5px;
    text-transform: uppercase;
    line-height: 1.2;
  }
  .holder__title {
    color: var(--text-soft);
    font-weight: 400; font-size: 14px; margin-top: 2px;
    line-height: 1.2;
  }
  .holder__rule {
    width: 58px; height: 2px; background: var(--accent-teal); margin-top: 8px;
  }
  .contacts {
    position: absolute; left: 40px; top: 166px;
    list-style: none;
    display: flex; flex-direction: column; gap: 6px;
  }
  .contact {
    display: flex; align-items: center; gap: 9px;
    color: var(--text-white); font-size: 11.5px; line-height: 1.25;
  }
  .contact__icon {
    flex: none; width: 19px; height: 19px; border-radius: 3px;
    background: var(--accent-teal);
    display: flex; align-items: center; justify-content: center;
  }
  .contact__icon svg { width: 12px; height: 12px; }
</style>
</head>
<body>
<main class="stage">
  <section class="card card--front">
    <div class="blueprint-art" role="img" aria-label="Faint blue architectural elevation drawing of a house"></div>
    <div class="brand"><span class="brand__mark"></span>Veltrow Drafts</div>
  </section>

  <section class="card card--back">
    <div class="blueprint-art" role="img" aria-label="Very faint blueprint drawing of a house elevation"></div>
    <div class="brand"><span class="brand__mark"></span>Veltrow Drafts</div>

    <div class="holder">
      <h1 class="holder__name">Dorian M. Halvek</h1>
      <p class="holder__title">Managing Director</p>
      <div class="holder__rule"></div>
    </div>

    <ul class="contacts">
      <li class="contact">
        <span class="contact__icon"><svg viewBox="0 0 12 12"><path d="M6 1a3.5 3.5 0 0 0-3.5 3.5C2.5 7 6 11 6 11s3.5-4 3.5-6.5A3.5 3.5 0 0 0 6 1z" fill="#fff"/><circle cx="6" cy="4.5" r="1.3" fill="#1aa39a"/></svg></span>
        <span>2713 Cypress Ridge Avenue<br>Florida, U.S. 32801</span>
      </li>
      <li class="contact">
        <span class="contact__icon"><svg viewBox="0 0 12 12"><path d="M3 1.5l1.8 2.3-1 1.2a6 6 0 0 0 3.2 3.2l1.2-1 2.3 1.8-1 1.5C5.5 10.5 1.5 6.5 1.5 2.5z" fill="#fff"/></svg></span>
        <span>+1 407 555 0192</span>
      </li>
      <li class="contact">
        <span class="contact__icon"><svg viewBox="0 0 12 12"><rect x="1.5" y="3" width="9" height="6" fill="none" stroke="#fff" stroke-width="1.2"/><path d="M1.5 3l4.5 3.5L10.5 3" fill="none" stroke="#fff" stroke-width="1.2"/></svg></span>
        <span>studio@veltrowdrafts.com</span>
      </li>
      <li class="contact">
        <span class="contact__icon"><svg viewBox="0 0 12 12"><path d="M2.5 2.5l7 3-3 1-1 3z" fill="#fff"/></svg></span>
        <span>www.veltrowdrafts.com</span>
      </li>
    </ul>
  </section>
</main>
</body>
</html>
```